Facebook Design Project

"Sun-Crest Coffee Kiosks" should be the page name.

Sun-Crest provides coffee carts, kiosks, and drive thrus to the Triangle (Raleigh/Durham, NC) serving the health conscious, on the go! We can set up in business offices/towers, campuses, hospitals, fitness centers or other high foot traffic locations. Sun-Crest offers certified, fair trade Nicaraguan coffee / espresso drinks, 100% fruit smoothies, protein shakes & healthy bites, to go!

Company will promote: health/wellness, protecting the environment & giving back to the community and to Nicaragua (10% of profits will help support Bright Path Outreach Nicaragua www.brightpathout.org )
Updates

I have updated my design needs. Thanks, Danielle

Target Market(s)

18-54, affluent coffee/espresso drinkers.

Industry/Entity Type

Environment

Requirements
Must have
• -Include my website (which is under construction) www.Sun-Crest.com
-Contact info: Email: danielle@sun-crest.com Phone number: 919-555-0147
-Twitter: @suncrestcoffee
-"Crest Tip of the day" This will be a daily wellness tip/post pertaining to nutrition, exercise and or mental well-being.

List:

"Organic Coffee & Espresso Drinks"
"100% Fruit Smoothies & Protein Shakes"
"Healthy Bites, To-Go"
"Fundraisers"
"Coffee Catering"

Tagline: "Break the fast!"
Nice to have
• I have attached my logo and business card (front and back). I would like to stay with same colors (dark brown, light brown and lime green)

-Put Sun-Crest's logo on a "to go" coffee cup but I would like it to look better than just the brown logo on a white cup. Maybe add the lime green color in some how. I have source files for the logo if you need to make changes.
Should not have
• Don't use cursive or weird fonts.

```html
<!DOCTYPE html>
<html lang="en">
<head>
<meta charset="utf-8">
<title>Sun-Crest Coffee Kiosks – Page Cover</title>
<link rel="stylesheet" href="https://fonts.googleapis.com/css2?family=Josefin+Sans:wght@400&family=Pathway+Gothic+One&display=swap">
<style>
  :root {
    --backdrop: #2a160c;
    --band-brown: #7a3f22;
    --lime: #a8cf3e;
    --dark-brown: #4a2a17;
    --mid-brown: #7a3f22;
    --contact-brown: #6b3a1f;
    --strip-white: #ffffff;
    --frame-grey: #c9c9c9;
  }
  * { margin: 0; padding: 0; box-sizing: border-box; }
  html, body {
    width: 1200px; height: 1000px; overflow: hidden;
    background: var(--backdrop);
  }
  .page {
    position: absolute; left: 47px; top: 260px;
    width: 1106px; height: 481px;
  }
  .cover-band {
    position: absolute; left: 0; top: 0; width: 1106px; height: 68px;
    background: var(--band-brown);
  }
  .cover-field {
    position: absolute; left: 0; top: 68px; width: 1106px; height: 341px;
    background: var(--lime);
  }
  .brand-mark {
    position: absolute; left: 527px; top: 26px;
    width: 100px; height: 100px; border-radius: 50%;
    background: var(--mid-brown);
  }
  .brand-name {
    position: absolute; left: 0; width: 1154px; top: 150px;
    text-align: center;
    font-family: "Josefin Sans", sans-serif; font-weight: 400;
    font-size: 92px; line-height: 1; color: var(--dark-brown);
  }
  .brand-sub, .brand-url, .brand-tagline {
    position: absolute; left: 0; width: 1154px; text-align: center;
    color: var(--mid-brown);
  }
  .brand-sub {
    top: 262px; font-family: "Josefin Sans", sans-serif;
    font-size: 20px; letter-spacing: 4px;
  }
  .brand-url {
    top: 290px; font-family: "Pathway Gothic One", sans-serif;
    font-size: 32px; letter-spacing: 1px;
  }
  .brand-tagline {
    top: 342px; font-family: "Josefin Sans", sans-serif;
    font-size: 27px; letter-spacing: 5px;
  }
  .contact-list {
    position: absolute; left: 880px; top: 280px; list-style: none;
    font-family: "Pathway Gothic One", sans-serif;
    font-size: 20px; line-height: 23px; color: var(--contact-brown);
  }
  .contact-list li { display: flex; align-items: center; gap: 6px; }
  .contact-list svg { width: 18px; height: 18px; flex: none; }
  .name-strip {
    position: absolute; left: 0; top: 409px; width: 1106px; height: 72px;
    background: var(--strip-white);
  }
  .page-name {
    position: absolute; left: 263px; top: 424px;
    font-family: "Pathway Gothic One", sans-serif;
    font-size: 36px; letter-spacing: 3px; color: #1a1a1a;
  }
  .profile-frame {
    position: absolute; left: 31px; top: 252px;
    width: 218px; height: 218px; padding: 5px;
    background: var(--strip-white); border: 1px solid var(--frame-grey);
  }
  .profile-art {
    width: 100%; height: 100%;
    background: linear-gradient(180deg, var(--lime) 0%, var(--lime) 55%, #b9c79a 80%, #8c6a50 100%);
  }
</style>
</head>
<body>
  <main class="page">
    <div class="cover-band"></div>
    <div class="cover-field"></div>

    <div class="brand-mark"></div>
    <h1 class="brand-name">Sun-Crest</h1>
    <p class="brand-sub">ORGANIC COFFEE</p>
    <p class="brand-url">www.Sun-Crest.com</p>
    <p class="brand-tagline">“BREAK THE FAST”</p>

    <ul class="contact-list">
      <li>
        <svg viewBox="0 0 18 18"><rect x="1" y="4" width="16" height="11" fill="var(--contact-brown)"/><path d="M1 4 L9 10 L17 4" fill="none" stroke="var(--lime)" stroke-width="1.5"/></svg>
        danielle@sun-crest.com
      </li>
      <li>
        <svg viewBox="0 0 18 18"><circle cx="9" cy="9" r="8" fill="none" stroke="var(--contact-brown)" stroke-width="1.5"/><path d="M6 5 L8 5 L8.5 7.5 L7.5 8.5 Q8.5 10.5 10 11 L11 10 L13 10.5 L13 12.5 Q8 13 5.5 7 Z" fill="var(--contact-brown)"/></svg>
        919-555-0147
      </li>
      <li>
        <svg viewBox="0 0 18 18"><circle cx="9" cy="9" r="7" fill="var(--contact-brown)"/></svg>
        @suncrestcoffee
      </li>
    </ul>

    <div class="name-strip"></div>
    <p class="page-name">Sun-Crest Coffee Kiosks</p>

    <div class="profile-frame">
      <div class="profile-art" role="img" aria-label="Profile image: coffee cup on a saucer with scattered beans beneath the brand symbol, on lime green"></div>
    </div>
  </main>
</body>
</html>
```